Plumbing Business Letterhead Design

Need a letterhead designed to use for my invoices and letters. I would like it to incorporate my business logo, which i will upload, and use light blue and grey colours. Or any colours that will work well with my logo (im not very good with art to know) . Also the letterhead needs to include the following:
Address - P.O Box 4826 Bega NSW 2550
Email - gareth@rwhitfieldplumbing.example.au
ABN - 41 906 572 338
Licence No. - 582061K
Mobile - 0412076584

Industry/Entity Type

Plumbing

Font styles to use
Sans Serif

Colors

Designer to choose colors to be used in the design.

```html
<!DOCTYPE html>
<html lang="en">
<head>
<meta charset="utf-8">
<title>Gareth Whitfield Plumbing – Letterhead</title>
<link rel="stylesheet" href="https://fonts.googleapis.com/css2?family=Arimo:wght@400;700&family=Bitter:wght@400&display=swap">
<style>
  :root {
    --paper: #ffffff;
    --ink: #1f1f1f;
    --brand-blue: #1c5a8e;
    --accent-line: #5aa9d6;
    --slate: #58595b;
    --orange: #f0931e;
    --footer-text: #f2f2f2;
  }
  * { margin: 0; padding: 0; box-sizing: border-box; }
  html, body { width: 939px; height: 1200px; overflow: hidden; background: var(--paper); }
  .letterhead {
    position: relative;
    width: 939px;
    height: 1200px;
    background: var(--paper);
    font-family: "Arimo", Arial, sans-serif;
    color: var(--ink);
  }
  .brand {
    position: absolute;
    left: 31px;
    top: 38px;
    display: flex;
    align-items: center;
    gap: 12px;
  }
  .brand-mark {
    width: 58px;
    height: 58px;
    background: var(--slate);
    border-radius: 6px;
  }
  .brand-name {
    font-family: "Arimo", Arial, sans-serif;
    font-weight: 700;
    font-size: 24px;
    line-height: 26px;
    color: var(--slate);
    text-transform: uppercase;
  }
  .contact {
    position: absolute;
    left: 578px;
    top: 37px;
    height: 85px;
    border-left: 1px solid var(--accent-line);
    padding-left: 20px;
    font-family: "Bitter", Georgia, serif;
    font-size: 13px;
    color: var(--ink);
    list-style: none;
  }
  .contact li { height: 26.5px; line-height: 26.5px; white-space: nowrap; }
  .contact .label { color: var(--brand-blue); margin-right: 6px; }
  .greeting {
    position: absolute;
    left: 28px;
    top: 218px;
    font-size: 16px;
    color: var(--brand-blue);
  }
  .subject {
    position: absolute;
    left: 28px;
    top: 267px;
    font-size: 17px;
    font-weight: 400;
    color: var(--brand-blue);
  }
  .body-copy {
    position: absolute;
    left: 28px;
    top: 328px;
    width: 803px;
    font-size: 14px;
    line-height: 24px;
    text-align: justify;
  }
  .body-copy p + p { margin-top: 21px; }
  .sign-off {
    position: absolute;
    left: 28px;
    top: 826px;
    font-size: 19px;
  }
  .signature {
    position: absolute;
    left: 37px;
    top: 868px;
    width: 145px;
    height: 46px;
    background: linear-gradient(90deg, #e9e9e9, #f5f5f5);
  }
  .footer-waves {
    position: absolute;
    left: 0;
    top: 0;
    width: 939px;
    height: 1200px;
    pointer-events: none;
  }
  .registration {
    position: absolute;
    top: 1152px;
    left: 475px;
    display: flex;
    align-items: center;
    font-family: "Bitter", Georgia, serif;
    font-size: 15px;
    color: var(--footer-text);
  }
  .registration .divider {
    width: 1px;
    height: 22px;
    background: var(--footer-text);
    opacity: .6;
    margin: 0 10px;
  }
</style>
</head>
<body>
<main class="letterhead">
  <header>
    <div class="brand">
      <span class="brand-mark"></span>
      <div class="brand-name">Gareth Whitfield<br>Plumbing</div>
    </div>
    <ul class="contact">
      <li><span class="label">C:</span>041 207 6584</li>
      <li><span class="label">E:</span>gareth@rwhitfieldplumbing.example.au</li>
      <li><span class="label">A:</span>P.O Box 4826 Bega, NSW 2550</li>
    </ul>
  </header>

  <p class="greeting">Hello Sir,</p>
  <h2 class="subject">Lorem ipsum dolor sit amet, consectetuer adipiscing elit, sed diam nonummy nibh</h2>

  <section class="body-copy">
    <p>Lorem ipsum dolor sit amet, consectetuer adipiscing elit, sed diam nonummy nibh euismod tincidunt ut laoreet dolore magna aliquam erat volutpat. Ut wisi enim ad minim veniam, quis nostrud exerci tation ullamcorper suscipit lobortis nisl ut aliquip ex ea commodo consequat. Duis autem vel eum iriure dolor in hendrerit in vulputate velit esse molestie consequat, vel illum dolore eu feugiat nulla facilisis at vero eros et accumsan et iusto odio dignissim qui blandit praesent luptatum zzril delenit augue duis dolore te feugait nulla facilisi.</p>
    <p>Lorem ipsum dolor sit amet, consectetuer adipiscing elit, sed diam nonummy nibh euismod tincidunt ut laoreet dolore magna aliquam erat volutpat. Ut wisi enim ad minim veniam, quis nostrud exerci tation ullamcorper suscipit lobortis nisl ut aliquip ex ea commodo consequat. Duis autem vel eum iriure dolor in hendrerit in vulputate velit esse molestie consequat, vel illum dolore eu feugiat nulla facilisis at vero eros et accumsan et iusto odio dignissim qui blandit praesent luptatum zzril delenit augue duis dolore te feugait nulla facilisi.</p>
    <p>Lorem ipsum dolor sit amet, consectetuer adipiscing elit, sed diam nonummy nibh euismod tincidunt ut laoreet dolore magna aliquam erat volutpat. Ut wisi enim ad minim veniam, quis nostrud exerci tation ullamcorper suscipit lobortis nisl ut aliquip ex ea commodo consequat. Duis autem vel eum iriure dolor in hendrerit in vulputate velit esse molestie consequat, vel illum dolore eu feugiat nulla facilisis at vero eros et accumsan et iusto odio dignissim qui blandit praesent luptatum zzril delenit augue duis dolore te feugait nulla facilisi.</p>
  </section>

  <p class="sign-off">Thank you</p>
  <div class="signature" role="img" aria-label="Handwritten signature of the sender"></div>

  <svg class="footer-waves" viewBox="0 0 939 1200" aria-hidden="true">
    <path fill="var(--slate)" d="M0 945 C8 1060 80 1120 230 1135 C380 1148 560 1100 700 1100 C800 1100 880 1150 939 1200 L0 1200 Z"/>
    <path fill="var(--paper)" d="M8 985 C30 1080 110 1125 240 1132 C400 1140 560 1092 700 1092 C800 1092 880 1140 935 1195 L939 1200 C880 1156 800 1108 700 1108 C560 1108 400 1158 230 1150 C90 1140 20 1080 8 985 Z"/>
    <path fill="var(--orange)" d="M10 1000 C35 1085 115 1122 240 1126 C400 1132 560 1082 700 1082 C800 1082 880 1130 939 1190 L939 1196 C880 1142 800 1096 700 1096 C560 1096 400 1146 240 1140 C100 1134 30 1090 10 1000 Z"/>
    <path fill="var(--paper)" d="M0 960 C20 1070 110 1110 240 1113 C330 1115 400 1100 450 1090 C400 1106 330 1124 240 1122 C100 1118 10 1070 0 995 Z"/>
  </svg>

  <footer class="registration">
    <span>ABN: 41 906 572 338</span>
    <span class="divider"></span>
    <span>Licence No.: 582061K</span>
  </footer>
</main>
</body>
</html>
```